Business Card Design and Logo Needed

I need Business Cards and a Logo for my website and public speaking business which can be found at: www.talia-ferrow.com

I'm looking for creative and unique ideas. Some business cards I've found online that I like can be found at:
http://gigmarketloft.com/general/18-smokin-hot-business-card-designs/

and at

http://www.theprintnookery.com/2009/04/50-creative-business-cards-of-50-graphic-designers/

```html
<!DOCTYPE html>
<html lang="en">
<head>
<meta charset="utf-8">
<title>Talia Ferrow – Business Card</title>
<link rel="stylesheet" href="https://fonts.googleapis.com/css2?family=Raleway:wght@100;200&family=Open+Sans:ital,wght@0,300;0,400;0,700;1,300&display=swap">
<style>
  :root {
    --olive: #3f5411;
    --olive-light: #8b9a3c;
    --paper: #ffffff;
    --frame: #7a8350;
  }
  * { margin: 0; padding: 0; box-sizing: border-box; }
  html, body {
    width: 1200px;
    height: 900px;
    overflow: hidden;
    background: var(--paper);
  }
  .canvas {
    position: relative;
    width: 1200px;
    height: 900px;
    font-family: "Open Sans", Arial, sans-serif;
  }
  .card {
    position: absolute;
    top: 34px;
    width: 416px;
    height: 830px;
  }
  .card--front {
    left: 116px;
    background: var(--olive);
    color: var(--paper);
  }
  .card--back {
    left: 664px;
    background: var(--paper);
    border: 2px solid var(--frame);
    color: var(--olive);
  }
  .brand-mark {
    position: absolute;
    font-weight: 300;
    font-size: 22px;
    line-height: 30px;
    white-space: nowrap;
  }
  .card--front .brand-mark { right: 46px; top: 590px; color: var(--paper); }
  .card--back .brand-mark { right: 44px; top: 608px; color: var(--olive-light); }
  .tagline {
    position: absolute;
    left: 44px;
    top: 680px;
    font-weight: 300;
    font-size: 21px;
    line-height: 28px;
    white-space: nowrap;
  }
  .name {
    position: absolute;
    left: 14px;
    top: 0;
    width: 120px;
    height: 560px;
  }
  .name text {
    font-family: "Raleway", "Helvetica Neue", sans-serif;
    font-weight: 100;
    font-size: 126px;
    fill: var(--olive);
  }
  .role {
    position: absolute;
    left: 124px;
    top: 44px;
    writing-mode: vertical-rl;
    font-style: italic;
    font-weight: 300;
    font-size: 18px;
    line-height: 24px;
    color: var(--olive-light);
    white-space: nowrap;
  }
  .contact {
    position: absolute;
    right: 44px;
    top: 676px;
    text-align: right;
    list-style: none;
  }
  .contact li {
    font-size: 21px;
    line-height: 40px;
    white-space: nowrap;
  }
  .contact .phone { font-weight: 700; }
</style>
</head>
<body>
<main class="canvas">
  <section class="card card--front" aria-label="Card front">
    <p class="brand-mark">Talia Ferrow</p>
    <p class="tagline">wonder. explore. dream. achieve</p>
  </section>

  <section class="card card--back" aria-label="Card back">
    <h1 class="name-heading">
      <svg class="name" viewBox="0 0 120 560" aria-label="Talia Ferrow">
        <text transform="rotate(-90)" x="-546" y="102" textLength="510" lengthAdjust="spacingAndGlyphs">TALIAFERROW</text>
      </svg>
    </h1>
    <p class="role">public speaker</p>
    <p class="brand-mark">Talia Ferrow</p>
    <ul class="contact">
      <li class="phone">0198 765 432</li>
      <li class="email">talia@talia-ferrow.com</li>
      <li class="web">www.talia-ferrow.com</li>
    </ul>
  </section>
</main>
</body>
</html>
```